Flyer-Design für Vegane und Gluten freie Haarpflege
Zielgruppe
Herstellung + Vertrieb von VEGANEN Haarpflegeprodukten
Shampoo, Conditioner Gluten frei und Vegan nicht an Tieren getestet und biologisch abbaubar
Aufgabenstellung
DIN 4 Grösse 2 Seiten Produktinformation für Verbraucher

```html
<!DOCTYPE html>
<html lang="de">
<head>
<meta charset="utf-8">
<title>PURA FOLIA – Vegane Haarpflege Flyer</title>
<link href="https://fonts.googleapis.com/css2?family=Montserrat:wght@300;400;600;700&display=swap" rel="stylesheet">
<style>
  :root{
    --bg:#dedede;
    --paper:#f4f4f5;
    --band:#7b7b7c;
    --band-text:#f1f1f1;
    --ink:#333336;
    --ink-soft:#6a6a6d;
    --rule:#8a8a8c;
    --leaf:#b3d36a;
    --photo-warm:#e7a521;
    --photo-cool:#7f7a9a;
    --bottle:#e9e9ec;
    --frame:#8d8d8f;
  }
  *{box-sizing:border-box;margin:0;padding:0}
  html,body{width:1200px;height:1077px;overflow:hidden;background:var(--bg)}
  body{position:relative;font-family:'Montserrat',sans-serif;color:var(--ink)}
  .spread{position:absolute;width:720px;height:510px;display:flex;box-shadow:0 10px 24px rgba(0,0,0,.18)}
  .spread--outer{left:150px;top:22px}
  .spread--inner{left:330px;top:545px}
  .panel{position:relative;width:240px;height:100%;background:var(--paper);overflow:hidden}
  .panel + .panel{border-left:1px solid #e2e2e4}
  .body-text{font-size:7px;line-height:1.32;text-align:justify;color:var(--ink)}
  .body-text p{margin-bottom:1px}
  .body-text strong{font-weight:700}
  .usage{padding:18px 14px 0 14px}
  .usage h1{font-weight:400;font-size:11.5px;letter-spacing:.2px;margin-bottom:8px}
  .usage h2{font-weight:700;font-size:7.3px;text-transform:uppercase;margin:8px 0 2px;line-height:1.25;text-align:justify}
  .band{background:var(--band);color:var(--band-text);display:flex;flex-direction:column;align-items:center}
  .brand{font-weight:300;text-transform:uppercase;letter-spacing:2px;color:var(--band-text);font-size:11px;display:flex;align-items:center;gap:6px}
  .brand-dot{width:6px;height:6px;border-radius:50%;background:var(--band-text)}
  .intro-band{height:230px;padding:72px 28px 0}
  .intro-band .brand{margin-bottom:30px}
  .intro-band p{font-size:7.4px;line-height:1.3;text-align:justify;color:var(--band-text);font-weight:300}
  .photo{display:block}
  .bottles-pair{position:absolute;left:20px;right:20px;top:258px;height:232px;background:linear-gradient(180deg,var(--paper),var(--bottle) 45%,#dcdcdf);border-radius:4px}
  .cover-band{height:238px;justify-content:center;padding-top:30px}
  .cover-band .brand{font-size:13px}
  .cover-title{margin:28px 30px 0;border-top:1px solid var(--rule);border-bottom:1px solid var(--rule);padding:10px 0;text-align:center}
  .cover-title h1{font-weight:400;font-size:21px;letter-spacing:.5px;color:var(--ink);margin-bottom:6px}
  .cover-title p{font-weight:300;font-size:8px;line-height:1.2;color:var(--ink-soft);text-transform:uppercase}
  .vegan-mark{position:relative;margin:30px auto 0;width:140px;height:50px}
  .vegan-mark .illustration-slot{position:absolute;left:40px;top:4px;width:80px;height:40px;background:var(--leaf)}
  .vegan-mark span{position:absolute;left:14px;top:14px;font-size:15px;font-weight:300;color:var(--ink)}
  .vegan-mark span b{font-weight:700}
  .cover-note{position:absolute;bottom:48px;left:0;right:0;text-align:center;font-weight:300;font-size:8px;line-height:1.3;color:var(--ink-soft)}
  .framed{position:absolute;left:10px;right:10px;top:10px;height:180px;border:4px solid var(--frame)}
  .framed .photo{width:100%;height:100%}
  .type-text{position:absolute;left:12px;right:12px}
  .bottle-row{position:absolute;left:22px;top:372px;width:436px;height:130px;background:linear-gradient(180deg,var(--paper),var(--bottle) 40%,#d9d9dc);border-radius:4px}
  .balance-band{position:absolute;left:10px;right:10px;top:10px;height:98px;justify-content:center;padding-top:34px}
  .badge{position:absolute;right:2px;top:2px;width:42px;height:42px;border-radius:50%;background:#fff;border:2px solid var(--leaf)}
  .illustration-corner{position:absolute;left:60px;bottom:22px;width:70px;height:30px;background:var(--leaf)}
</style>
</head>
<body>

<section class="spread spread--outer" aria-label="Außenseite">
  <article class="panel usage">
    <h1>ANWENDUNG VON PURA FOLIA</h1>
    <div class="body-text">
      <h2>So wasche ich meine Haare</h2>
      <p>EQUILIBRA reinigt und schützt. EQUILIBRA auf die trockene Haare auftragen. Er hat die Eigenschaft den pH Wert und damit die Ladung des Haares zu verändern. Anlagerungen wie Festiger, Haarspray und Schmutzpartikel werden während des anfeuchten vom Haar gelöst. Das Haar ist angefeuchtet und ohne Einsatz von Shampoo gewaschen.<br>EQUILIBRA schützt das Haar, macht es geschmeidig und neutralisiert den pH- Wert.</p>
      <h2>So wasche ich meine Kopfhaut</h2>
      <p>Man nimmt eine walnussgrosse Menge PURA FOLIA Shampoo und verteilt es, vom Haaransatz zum Oberkopf, gleichmässig mit den Fingern auf der Kopfhaut. Gut massieren und wieder ausspülen. Schäumt das PURA FOLIA Shampoo nicht, wiederholt man den Vorgang solange, bis Schaum entsteht. Erst wenn Schaum entsteht ist gewährleistet, dass alle Rückstände auf der Kopfhaut gebunden sind. Lieber viermal mit wenig, als einmal mit viel Shampoo oberflächlich waschen. Dadurch erhält man 30% mehr Volumen.</p>
      <h2>Warum ist die Neutralisation von Haaren und Kopfhaut nach dem Waschen wichtig?</h2>
      <p>Nach dem waschen der Kopfhaut, oder nach der Behandlung mit einer Intensiv Mask neutralisiert man die Haare, damit die Schuppenschicht geschlossen und der pHWert von Haut und Haar eingestellt wird.<br>Man löst PURA FOLIA Equilibra in ca. 200 ml Wasser auf. Das jetzt ionisierte Wasser gibt man auf Kopfhaut und Haare.<br>Anschliessend spült man, mit kühlerem Wasser, die Haare gut aus.<br>Tägliches bürsten von Haar und Kopfhaut bindet Fette und löst Ablagerungen auf der Kopfhaut. Jeden Morgen bis zu 100 Bürstenstriche für eine gesunde Kopfhaut und glänzende Haare.</p>
    </div>
  </article>

  <article class="panel">
    <div class="band intro-band">
      <div class="brand"><span class="brand-dot"></span>Lena Marwitz</div>
      <p>Lorem ipsum dolor sit amet, consetetur sadipscing elitr, sed diam nonumy eirmod tempor invidunt ut labore et dolore magna aliquyam erat, sed diam voluptua.<br>At vero eos et accusam et justo duo dolores et ea rebum.</p>
    </div>
    <div class="photo bottles-pair" role="img" aria-label="Produktfoto: zwei weiße Shampooflaschen mit grauem Deckel"></div>
  </article>

  <article class="panel">
    <div class="band cover-band">
      <div class="brand"><span class="brand-dot"></span>Lena Marwitz</div>
    </div>
    <div class="cover-title">
      <h1>PURA FOLIA</h1>
      <p>Mit edlen Rohstoffen<br>aus nachhaltigen Ressourcen</p>
    </div>
    <div class="vegan-mark">
      <div class="illustration-slot" role="img" aria-label="Platz für grüne Blattillustration"></div>
      <span>100%<b>Vegan</b></span>
    </div>
    <p class="cover-note">ohne Tierversuche<br>und biologisch abbaubar</p>
  </article>
</section>

<section class="spread spread--inner" aria-label="Innenseite">
  <article class="panel">
    <div class="framed"><div class="photo" style="background:radial-gradient(circle at 50% 45%,#f2c040,var(--photo-warm))" role="img" aria-label="Porträtfoto: lachende Frau mit Lockenkopf und Brille vor gelbem Hintergrund"></div></div>
    <div class="type-text body-text" style="top:200px">
      <p><strong>Bei Afrikanischen, Asiatischen &amp; Mediterranen Typen</strong> ist die Sonnenstrahlung intensiver die Haut wird dunkler. Sie produziert nun viel mehr Farbpigmente um die Haut vor der starken Sonneneinstrahlung zu schützen.<br>Durch Sonne und Wärme transpiriert der Körper. Salze und Feuchtigkeit die werden dem Körper entzogen.<br>Daher neigen Menschen im Süden mehr zur trockener Haut-. Die Pflege der Kopfhaut und der Haare sollten mehr feuchtigkeitsspendet sein.</p>
      <p style="margin-top:8px">PURA FOLIA Shampoo <strong>sicca lenis</strong> ist Gluten frei und Vegan, nicht an Tieren getestet und biologisch abbaubar.</p>
    </div>
  </article>

  <article class="panel">
    <div class="band balance-band">
      <div class="brand"><span class="brand-dot"></span>Lena Marwitz</div>
      <div class="badge" role="img" aria-label="Siegel vegan"></div>
    </div>
    <div class="type-text body-text" style="top:122px">
      <p>Es ist ganz einfach, um Säure auszugleichen braucht man Base. Um Base zu neutralisieren benötigt man Säure.<br>Daher muss man vor und nach dem Haare waschen immer einen pHAusgleich machen.<br>Der Equilibra ist ein Muss vor und nach jeglicher Kopf- und Haarwäsche um die Kopfhaut zu neutralisieren müssen Shampoos entweder etwas saurerer oder basischer eingestellt sein, somit kann die Kopfhaut schon während der Reinigung auf den neutralen pH- Wert zurückgeführt werden.</p>
      <p style="margin-top:8px">PURA FOLIA <strong>Equilibra</strong> ist Gluten frei und Vegan, nicht an Tieren getestet und biologisch abbaubar.</p>
    </div>
  </article>

  <article class="panel">
    <div class="framed" style="left:12px;right:12px;height:168px;border-width:3px"><div class="photo" style="background:linear-gradient(160deg,#9a93b0,var(--photo-cool) 55%,#c9a98a)" role="img" aria-label="Porträtfoto: Frau mit langem blondem Haar vor violettem Hintergrund"></div></div>
    <div class="type-text body-text" style="top:190px">
      <p><strong>Die Keltischen, Nordischen &amp; Mittel-europäischen Typen</strong> haben eine höhere Fettproduktion um sich vor Kälte zu schützen.<br>Genetisch bedingt findet man diese Haartypen eher in östlichen und nördlichen Regionen.<br>Im Norden ist es kälter als am Äquator, weil der Einstrahlwinkel der Sonnenstrahlen kleiner und damit die Fläche, die von einem bestimmten Sonnenstrahlbündel beschienen wird, größer ist.</p>
      <p style="margin-top:8px">PURA FOLIA Shampoo <strong>pinguis lenis</strong> ist Gluten frei und Vegan, nicht an Tieren getestet und biologisch abbaubar.</p>
    </div>
    <div class="illustration-corner" role="img" aria-label="Platz für grüne Blattillustration"></div>
  </article>

  <div class="photo bottle-row" role="img" aria-label="Produktfoto: fünf weiße Flaschen der Produktreihe"></div>
</section>

</body>
</html>
```